Business card for new business - financial management

I need a business card designed for my new business. I'm the owner / sole trader of QVB Consulting, which provides financial management services for Government. I'd like the design to incorporate the attached business name and colours. The design should include colour and not be too way out - it needs to look at home in a government environment.
Details to be included on the card are:
QVB Consulting
Miriam Haskett
0400 386 924
miriamrhaskett@fernmail.example
47 Pallister Crescent, Wendlow ACT 2911
Single or double sided designs would be good.
Employees at Australian Federal Government agencies
Government

```html
<!DOCTYPE html>
<html lang="en">
<head>
<meta charset="utf-8">
<title>QVB Consulting – Business Card</title>
<link rel="stylesheet" href="https://fonts.googleapis.com/css2?family=Open+Sans:wght@400;600&display=swap">
<style>
  :root {
    --stage: #d9d9d9;
    --card-dark: #2b2b2c;
    --card-dark-edge: #363637;
    --card-light: #ffffff;
    --accent: #8ccbd6;
    --brand-blue: #245c8f;
    --text-light: #f2f2f2;
    --icon-ink: #2b2b2c;
  }
  * { box-sizing: border-box; margin: 0; padding: 0; }
  html, body {
    width: 1200px; height: 900px; overflow: hidden;
    background: var(--stage);
    font-family: "Open Sans", Arial, sans-serif;
  }
  .canvas { position: relative; width: 1200px; height: 900px; }

  .card {
    position: absolute; left: 285px; width: 630px; height: 360px;
    overflow: hidden;
    box-shadow: 0 8px 24px rgba(0,0,0,0.18);
  }
  .card--back { top: 60px; }
  .card--front { top: 480px; background: var(--card-light); }

  .back-texture {
    position: absolute; inset: 0;
    background: radial-gradient(circle at 60% 40%, var(--card-dark-edge), var(--card-dark));
  }
  .accent-bar {
    position: absolute; left: 127px; width: 26px; background: var(--accent);
  }
  .accent-bar--top { top: 0; height: 118px; border-radius: 0 0 13px 13px; }
  .accent-bar--bottom { top: 278px; bottom: 0; border-radius: 13px 13px 0 0; }

  .identity { position: absolute; left: 168px; top: 42px; }
  .identity__name { font-size: 26px; font-weight: 400; color: var(--accent); line-height: 1.15; }
  .identity__company { font-size: 16px; line-height: 1.3; color: var(--text-light); }

  .contact-list { position: absolute; left: 126px; top: 142px; list-style: none; }
  .contact-list__item {
    display: flex; align-items: center; gap: 14px;
    height: 28px; margin-bottom: 16px;
    color: var(--text-light); font-size: 13px; white-space: nowrap;
  }
  .contact-list__icon {
    flex: 0 0 28px; width: 28px; height: 28px; border-radius: 50%;
    background: var(--accent);
    display: flex; align-items: center; justify-content: center;
  }
  .contact-list__icon svg { width: 16px; height: 16px; }
  .icon-fill { fill: var(--icon-ink); }
  .icon-line { fill: none; stroke: var(--icon-ink); stroke-width: 2; stroke-linejoin: round; }

  .front-band { position: absolute; height: 46px; background: var(--accent); }
  .front-band--left { left: 0; top: 40px; width: 130px; border-radius: 0 23px 23px 0; }
  .front-band--right { right: 0; top: 222px; width: 140px; border-radius: 23px 0 0 23px; }

  .brand-name {
    position: absolute; left: 150px; top: 118px;
    font-size: 50px; font-weight: 600; color: var(--brand-blue);
    letter-spacing: 0.5px; white-space: nowrap; line-height: 1.2;
  }
</style>
</head>
<body>
<main class="canvas">

  <section class="card card--back" aria-label="Card back with contact details">
    <div class="back-texture" role="img" aria-label="Dark charcoal background with a subtle dotted texture"></div>
    <div class="accent-bar accent-bar--top"></div>
    <div class="accent-bar accent-bar--bottom"></div>

    <div class="identity">
      <p class="identity__name">Miriam Haskett</p>
      <p class="identity__company">QVB Consulting</p>
    </div>

    <ul class="contact-list">
      <li class="contact-list__item">
        <span class="contact-list__icon">
          <svg viewBox="0 0 24 24" aria-hidden="true"><path class="icon-fill" d="M6.6 10.8a15.1 15.1 0 0 0 6.6 6.6l2.2-2.2a1 1 0 0 1 1-.25 11.4 11.4 0 0 0 3.6.57 1 1 0 0 1 1 1V20a1 1 0 0 1-1 1A17 17 0 0 1 3 4a1 1 0 0 1 1-1h3.5a1 1 0 0 1 1 1c0 1.25.2 2.45.57 3.57a1 1 0 0 1-.25 1z"/></svg>
        </span>
        <span>0400 386 924</span>
      </li>
      <li class="contact-list__item">
        <span class="contact-list__icon">
          <svg viewBox="0 0 24 24" aria-hidden="true"><rect class="icon-line" x="3" y="6" width="18" height="12" rx="1"/><path class="icon-line" d="M3.5 6.5 12 13l8.5-6.5"/></svg>
        </span>
        <span>miriamrhaskett@fernmail.example</span>
      </li>
      <li class="contact-list__item">
        <span class="contact-list__icon">
          <svg viewBox="0 0 24 24" aria-hidden="true"><path class="icon-fill" d="M12 3 2 12h3v8h5v-5h4v5h5v-8h3z"/></svg>
        </span>
        <span>47 Pallister Crescent, Wendlow ACT 2911</span>
      </li>
    </ul>
  </section>

  <section class="card card--front" aria-label="Card front with business name">
    <div class="front-band front-band--left"></div>
    <p class="brand-name">QVB Consulting</p>
    <div class="front-band front-band--right"></div>
  </section>

</main>
</body>
</html>
```